Business card for technical support company.
FixWiseDesk.com
Business card for technical support company.  - Computers
Creative Brief
Use specific fonts
Up To designer
Professional
Marcus Bell
VP In Charge
482 Alder Lane New York, NY 48213
service@FixWiseDesk.com
This will be used as a mock-up for my business card. Editable Adobe Illustrator or comparable original design file will need to be included with the final design. Also logo can be broken up from the FixWiseDesk.com below it and arranged on the card.
Company logo, website, and possible list of services. Please allow room to add later. 5-6 bullet points
qm71xrb qm71xrb
Nice first drafts everyone. I would like to see how some of these look with a white background instead of black. Nice!
I would like one design but two separate color schemes. Please match the two color schemes of the example logos provided. Thank you!

```html
<!DOCTYPE html>
<html lang="en">
<head>
<meta charset="utf-8">
<title>FixWiseDesk Business Cards</title>
<link href="https://fonts.googleapis.com/css2?family=Montserrat:wght@400;600;700&display=swap" rel="stylesheet">
<style>
  :root{
    --stage:#e9e7e3;
    --charcoal:#3b3c3f;
    --charcoal-dark:#2c2d30;
    --white:#ffffff;
    --blue:#1f7fe0;
    --blue-deep:#0b4fb3;
    --blue-light:#59b4ff;
    --silver:#c9ccd1;
    --ink-light:#d8dade;
    --ink-dark:#5a5d63;
  }
  *{margin:0;padding:0;box-sizing:border-box}
  html,body{width:1200px;height:978px;overflow:hidden}
  body{background:var(--stage);position:relative;font-family:"Montserrat",sans-serif}
  .card{position:absolute;width:560px;height:320px;border-radius:18px;overflow:hidden;box-shadow:0 10px 30px rgba(0,0,0,.18)}
  .card--front{left:70px;top:150px;background:var(--charcoal)}
  .card--back{left:570px;top:508px;background:var(--white)}
  .card__band{position:absolute;inset:0;width:100%;height:100%}
  .brand{position:absolute;display:flex;align-items:center;gap:12px}
  .brand__mark{width:22px;height:22px;background:var(--blue)}
  .brand__name{font-weight:700;font-size:26px;letter-spacing:.5px}
  .card--front .brand{left:42px;top:118px}
  .card--front .brand__name{color:var(--blue-light)}
  .card--back .brand{left:50%;top:126px;transform:translateX(-50%)}
  .card--back .brand__name{color:var(--blue-deep)}
  .contact{position:absolute;left:306px;top:34px;color:var(--ink-light);font-size:10px;line-height:1.55}
  .contact__name{font-weight:700;font-size:12px;text-transform:uppercase;letter-spacing:.6px;color:var(--white)}
  .contact__title{font-size:9px;margin-bottom:10px;color:var(--silver)}
  .contact__address{margin-bottom:10px}
  .contact__row{display:flex;align-items:center;gap:7px}
  .contact__row svg{width:10px;height:10px;fill:var(--blue-light)}
</style>
</head>
<body>

<div class="card card--front">
  <svg class="card__band" viewBox="0 0 560 320" preserveAspectRatio="none" aria-hidden="true">
    <defs>
      <linearGradient id="frontBand" x1="0" y1="0" x2="1" y2="0">
        <stop offset="0" stop-color="#0b4fb3"/>
        <stop offset=".5" stop-color="#2f93f0"/>
        <stop offset="1" stop-color="#0b4fb3"/>
      </linearGradient>
    </defs>
    <path d="M0 262 Q280 248 560 220 L560 320 L0 320 Z" fill="url(#frontBand)"/>
    <path d="M0 256 Q280 242 560 214 L560 222 Q280 250 0 264 Z" fill="#8f949b"/>
    <line x1="284" y1="30" x2="250" y2="240" stroke="#6f7379" stroke-width="1.2"/>
  </svg>
  <div class="brand">
    <span class="brand__mark"></span>
    <span class="brand__name">FixWiseDesk</span>
  </div>
  <div class="contact">
    <p class="contact__name">Marcus Bell</p>
    <p class="contact__title">VP In Charge</p>
    <p class="contact__address">482 Alder Lane<br>New York, NY 48213</p>
    <p class="contact__row">
      <svg viewBox="0 0 10 10"><path d="M2 0h2l1 3-1.5 1a6 6 0 0 0 2.5 2.5L7 5l3 1v2c0 1-1 2-2 2A8 8 0 0 1 0 2c0-1 1-2 2-2z"/></svg>
      (212) 555-0147
    </p>
    <p class="contact__row">
      <svg viewBox="0 0 10 10"><rect x="1" y="0" width="8" height="10" rx="1.5"/></svg>
      (212) 555-0198
    </p>
    <p class="contact__row">
      <svg viewBox="0 0 10 10"><path d="M0 2h10v6H0z M0 2l5 3.5L10 2" /></svg>
      service@FixWiseDesk.com
    </p>
    <p class="contact__row">
      <svg viewBox="0 0 10 10"><circle cx="5" cy="5" r="4.5"/></svg>
      www.FixWiseDesk.com
    </p>
  </div>
</div>

<div class="card card--back">
  <svg class="card__band" viewBox="0 0 560 320" preserveAspectRatio="none" aria-hidden="true">
    <defs>
      <linearGradient id="backBand" x1="0" y1="0" x2="0" y2="1">
        <stop offset="0" stop-color="#0b4fb3"/>
        <stop offset=".5" stop-color="#2f93f0"/>
        <stop offset="1" stop-color="#0b4fb3"/>
      </linearGradient>
    </defs>
    <path d="M0 0 L0 320 L30 320 Q18 160 24 0 Z" fill="url(#backBand)"/>
    <path d="M24 0 Q18 160 30 320 L38 320 Q26 160 32 0 Z" fill="#a9adb3"/>
  </svg>
  <div class="brand">
    <span class="brand__mark"></span>
    <span class="brand__name">FixWiseDesk</span>
  </div>
</div>

</body>
</html>
```